I need an infographic design about drug use in college

We require an infographic design for an article about drug use by college students.
The infographic will be titled: "Increasing Numbers of College Students Drink", and will include numerical data. We will provide the content and data.
Size: The infographic will be posted on this site: http://velmorquay.com, and should fit the width of its inner pages (and be readable, of course).
Color palate: Nothing specific in mind - it should be eye-catching, yet understated.
The infographic should be highly professional, and VERY eye-catching.
Here are some examples of infographic designs I like:
http://www.pendraxiloft.com/wp-content/uploads/2013/02/Youth-Sports-Injuries.png
http://image.grumtavel.com/display_pic_with_logo/607969/97564355/stock-vector-sports-complex-infographics-97564355.jpg
http://quorvandelle.com/wp-content/uploads/2011/10/transparency.jpg
Priority will be given to designers who show a portfolio that includes infographic designs.
ATTACHED IS THE CONTENT FOR THE INFOGRAPHIC.

```html
<!DOCTYPE html>
<html lang="en">
<head>
<meta charset="utf-8">
<title>Increasing Number of College Students Drink</title>
<link href="https://fonts.googleapis.com/css2?family=Josefin+Sans:wght@400;600;700&family=Nunito:wght@600;700;800;900&display=swap" rel="stylesheet">
<style>
:root{
  --plum:#45262f;
  --berry:#92204e;
  --yellow:#f5e22a;
  --orange:#e6743a;
  --mint:#e0efd6;
  --white:#ffffff;
  --ink:#45262f;
  --grey:#5a5a5a;
}
html,body{margin:0;padding:0;width:1200px;height:4581px;overflow:hidden;background:var(--white);}
.board{width:675px;height:2577px;position:relative;transform:scale(1.77778);transform-origin:0 0;font-family:'Nunito',sans-serif;color:var(--ink);}
.board > section{position:absolute;left:0;width:675px;}
.abs{position:absolute;}

/* header */
.header{top:0;height:290px;background:var(--plum);}
.tap-art{left:0;top:0;width:190px;height:225px;background:linear-gradient(180deg,#e6743a,#c85f2c);border-radius:0 0 40px 0;opacity:.9;}
.title-top{right:40px;top:36px;text-align:right;color:var(--white);font-family:'Josefin Sans',sans-serif;font-weight:600;font-size:38px;line-height:43px;letter-spacing:1px;}
.title-drink{right:40px;top:112px;color:var(--yellow);font-family:'Josefin Sans',sans-serif;font-weight:700;font-size:92px;line-height:90px;letter-spacing:30px;margin-right:-30px;}
.wave{left:0;top:235px;}

/* intro */
.intro{top:290px;height:182px;background:var(--yellow);}
.intro p{position:absolute;left:18px;right:18px;top:68px;margin:0;text-align:center;font-weight:800;font-size:17.5px;line-height:29px;color:var(--ink);}
.bubble{position:absolute;border-radius:50%;background:var(--white);}

.source-band{top:472px;height:46px;background:var(--orange);}
.source-band p{margin:0;line-height:46px;text-align:center;color:var(--white);font-family:'Josefin Sans',sans-serif;font-weight:600;font-size:17px;letter-spacing:.3px;}

/* 80% */
.consume{top:518px;height:372px;background:var(--berry);}
.stat-80{left:45px;top:28px;color:var(--white);font-weight:800;font-size:80px;line-height:80px;}
.stat-80-cap{left:46px;top:110px;color:var(--white);font-weight:700;font-size:18px;}
.caps-box{left:0;top:144px;width:365px;height:203px;background:var(--white);}
.caps-art{left:48px;top:20px;width:290px;height:160px;border-radius:6px;background:linear-gradient(180deg,#4b4b4b 0%,#4b4b4b 66%,#bdbdbd 100%);}
.glass-art{left:485px;top:92px;width:155px;height:262px;border-radius:60px 60px 12px 12px;background:linear-gradient(180deg,#ffffff 0%,#d8ebcb 40%,#6b1634 60%,#d8ebcb 100%);}

/* binge */
.binge{top:890px;height:405px;background:var(--mint);}
.binge-card{left:50px;top:22px;width:578px;height:280px;background:var(--white);box-shadow:7px 7px 0 var(--orange);}
.ribbon{left:316px;top:-8px;}
.pct-42{left:40px;top:205px;width:190px;text-align:center;font-weight:700;font-size:17.5px;line-height:21px;color:var(--ink);}
.pct-42 b{color:var(--berry);font-weight:900;font-size:27px;}
.person-art{width:30px;height:82px;background:#3c2a2f;border-radius:14px;}
.glass-row{left:350px;}
.two-hours{left:362px;top:166px;font-weight:700;font-size:13px;color:var(--ink);}
.binge-note{left:48px;right:48px;top:316px;margin:0;text-align:justify;text-align-last:center;font-weight:600;font-size:17.5px;line-height:22px;color:var(--grey);}

/* frightening */
.fright{top:1295px;height:300px;background:var(--plum);}
.fright-head{left:120px;top:34px;color:var(--white);font-weight:800;font-size:22.5px;line-height:29px;}
.cloud{left:0;top:95px;}
.two-five{left:0;right:0;top:153px;text-align:center;font-weight:800;font-size:21.5px;color:var(--ink);}
.faces-art{left:120px;top:200px;width:440px;height:95px;border-radius:40px;background:linear-gradient(90deg,#fbe3cf,#f4d0b6);}

/* lifetime */
.lifetime{top:1595px;height:325px;background:var(--yellow);}
.pillar{position:absolute;width:28px;height:195px;border-radius:10px;background:#f1b633;top:110px;}
.big-num{font-weight:900;font-size:78px;line-height:78px;color:var(--plum);text-align:center;}
.big-cap{font-weight:800;font-size:22px;line-height:27px;color:var(--plum);text-align:center;}
.orange-strip{top:1920px;height:40px;background:var(--orange);}

/* ages */
.ages{top:1960px;height:540px;background:var(--berry);}
.ages h2{position:absolute;left:0;right:0;top:24px;margin:0;text-align:center;color:var(--white);font-family:'Josefin Sans',sans-serif;font-weight:600;font-size:37px;letter-spacing:.5px;}
.plate{position:absolute;top:112px;width:190px;height:100px;background:var(--yellow);box-sizing:border-box;border:5px solid var(--yellow);}
.plate-inner{position:absolute;inset:0;border:3px solid var(--plum);text-align:center;}
.plate-num{margin-top:17px;font-family:'Josefin Sans',sans-serif;font-weight:600;font-size:35px;line-height:36px;color:var(--plum);}
.plate-unit{font-family:'Josefin Sans',sans-serif;font-weight:600;font-size:15px;color:var(--plum);}
.rivet{position:absolute;width:6px;height:6px;border-radius:50%;background:var(--plum);top:6px;}
.plate-arrow{position:absolute;top:238px;}
.outcome{position:absolute;top:315px;width:200px;text-align:center;color:var(--white);font-weight:800;font-size:19px;line-height:26px;}

/* footer */
.footer{top:2500px;height:60px;background:var(--white);}
.brand{left:0;right:0;top:14px;display:flex;justify-content:center;align-items:center;gap:12px;}
.brand-dot{width:26px;height:26px;border-radius:50%;background:var(--berry);}
.brand-name{font-family:'Josefin Sans',sans-serif;font-weight:600;font-size:24px;letter-spacing:4px;color:var(--plum);}
.bottom-strip{top:2560px;height:17px;background:var(--yellow);}
</style>
</head>
<body>
<div class="board">

  <section class="header">
    <div class="abs tap-art" role="img" aria-label="Illustration of an orange beer tap dripping a drop of beer"></div>
    <div class="abs title-top">INCREASING NUMBER OF<br>COLLEGE STUDENTS</div>
    <div class="abs title-drink">DRINK</div>
    <svg class="abs wave" width="675" height="60" viewBox="0 0 675 60" aria-hidden="true">
      <path d="M0 22 Q22 52 45 22 T90 22 T135 22 T180 22 T225 22 T270 22 T315 22 T360 22 T405 22 T450 22 T495 22 T540 22 T585 22 T630 22 T675 22 V60 H0 Z" fill="#f5e22a"/>
    </svg>
  </section>

  <section class="intro">
    <span class="bubble" style="left:108px;top:30px;width:12px;height:12px"></span>
    <span class="bubble" style="left:145px;top:52px;width:16px;height:16px"></span>
    <span class="bubble" style="left:333px;top:26px;width:22px;height:22px"></span>
    <span class="bubble" style="left:560px;top:42px;width:14px;height:14px"></span>
    <span class="bubble" style="left:34px;top:140px;width:18px;height:18px"></span>
    <span class="bubble" style="left:620px;top:148px;width:14px;height:14px"></span>
    <p>One area where students have the opportunity to experiment is with their use of alcohol. Though colleges do not endorse drinking for students under the legal drinking age, students find ways to access alcohol.</p>
  </section>

  <section class="source-band"><p>HALVERN INSTITUTE ON ALCOHOL STUDIES STATICS</p></section>

  <section class="consume">
    <div class="abs stat-80">80%</div>
    <div class="abs stat-80-cap">of college students consume alcohol</div>
    <svg class="abs" style="left:370px;top:38px" width="200" height="90" viewBox="0 0 200 90" aria-hidden="true">
      <path d="M4 82 H52 V4 H193 V40" fill="none" stroke="#f5e22a" stroke-width="2.5" stroke-dasharray="3 4"/>
      <path d="M186 38 L193 48 L200 38 Z" fill="#f5e22a"/>
    </svg>
    <div class="abs caps-box">
      <div class="abs caps-art" role="img" aria-label="Ten graduation cap icons, eight dark and two light"></div>
    </div>
    <div class="abs glass-art" role="img" aria-label="Illustration of a wine glass filled with red wine"></div>
  </section>

  <section class="binge">
    <div class="abs binge-card">
      <svg class="abs" style="left:38px;top:30px" width="160" height="160" viewBox="-80 -80 160 160" aria-hidden="true">
        <circle r="78" fill="#92204e"/>
        <path d="M0 0 L-56 -54 A78 78 0 0 0 12 77 Z" fill="#e6743a" transform="translate(-6 4)"/>
        <path d="M0 0 L-54 -56" stroke="#fff" stroke-width="5"/>
        <path d="M0 0 L12 77" stroke="#fff" stroke-width="5"/>
      </svg>
      <svg class="abs" style="left:208px;top:90px" width="100" height="80" viewBox="0 0 100 80" aria-hidden="true">
        <path d="M2 4 H58 V72 H64" fill="none" stroke="#e6743a" stroke-width="2" stroke-dasharray="2 3"/>
        <path d="M70 66 Q66 72 70 78" fill="none" stroke="#45262f" stroke-width="1.5"/>
      </svg>
      <div class="abs person-art" style="left:300px;top:68px" role="img" aria-label="Male figure icon"></div>
      <div class="abs person-art" style="left:296px;top:180px;width:38px" role="img" aria-label="Female figure icon"></div>
      <svg class="abs glass-row" style="top:100px" width="210" height="30" viewBox="0 0 210 30" aria-hidden="true">
        <g fill="#45262f">
          <path id="mg" d="M0 2 H28 L15 16 V25 H21 V28 H7 V25 H13 V16 Z"/>
          <use href="#mg" x="45"/><use href="#mg" x="90"/><use href="#mg" x="135"/><use href="#mg" x="180"/>
        </g>
      </svg>
      <div class="abs two-hours">consume in two hours or less</div>
      <svg class="abs glass-row" style="top:208px" width="170" height="30" viewBox="0 0 170 30" aria-hidden="true">
        <g fill="#45262f">
          <use href="#mg" x="0"/><use href="#mg" x="45"/><use href="#mg" x="90"/><use href="#mg" x="135"/>
        </g>
      </svg>
      <div class="abs pct-42"><b>42%</b> of full-time college students report ‘binge drinking’</div>
    </div>
    <svg class="abs ribbon" width="345" height="70" viewBox="0 0 345 70" aria-hidden="true">
      <path d="M0 45 L30 32 L30 58 L14 70 Z" fill="#e6743a"/>
      <path d="M300 5 L345 -5 L330 25 L340 50 L300 40 Z" fill="#e6743a"/>
      <path d="M14 30 L310 0 L310 48 L14 70 Z" fill="#e6743a"/>
      <text x="40" y="48" transform="rotate(-5 160 40)" fill="#fff" font-family="Josefin Sans, sans-serif" font-weight="600" font-size="25" letter-spacing="1">BINGE DRINKING</text>
    </svg>
    <p class="abs binge-note">On a slightly more positive note, binge drinking is seemingly on the decrease in the late high school years, primarily among grade 12 boys, which will hopefully lead to lower stats at college level.</p>
  </section>

  <section class="fright">
    <svg class="abs" style="left:6px;top:52px" width="104" height="16" viewBox="0 0 104 16" aria-hidden="true">
      <path d="M0 8 H88" stroke="#fff" stroke-width="3" stroke-dasharray="3 5"/>
      <path d="M92 1 L104 8 L92 15 Z" fill="#fff"/>
    </svg>
    <div class="abs fright-head">But for now, the stats are<br>quite frightening:</div>
    <svg class="abs cloud" width="675" height="210" viewBox="0 0 675 210" aria-hidden="true">
      <path d="M0 35 Q40 0 90 25 Q150 -10 210 22 Q270 -12 330 20 Q390 -8 440 18 Q500 -14 560 18 Q620 -6 675 20 V210 Q620 225 560 200 Q500 230 440 205 Q380 230 320 205 Q260 230 200 205 Q140 230 80 205 Q40 220 0 205 Z" fill="#fff"/>
    </svg>
    <div class="abs two-five">Two out of five college youths engage in binge drinking</div>
    <div class="abs faces-art" role="img" aria-label="Row of five cartoon student heads, two of them dizzy"></div>
  </section>

  <section class="lifetime">
    <span class="bubble" style="left:395px;top:112px;width:14px;height:14px"></span>
    <span class="bubble" style="left:438px;top:270px;width:24px;height:24px"></span>
    <span class="bubble" style="left:575px;top:215px;width:10px;height:10px"></span>
    <div class="pillar" style="left:52px"></div>
    <div class="pillar" style="left:322px"></div>
    <div class="pillar" style="left:608px"></div>
    <div class="abs" style="left:82px;top:110px;width:225px">
      <div class="big-num">78%</div>
      <div class="big-cap">of college students have tried alcohol at least once in their lifetime.</div>
    </div>
    <div class="abs" style="left:370px;top:110px;width:230px">
      <div class="big-num">66%</div>
      <div class="big-cap">report they have been drunk</div>
    </div>
  </section>

  <section class="orange-strip"></section>

  <section class="ages">
    <h2>BETWEEN THE AGES OF 18 AND 24</h2>

    <div class="plate" style="left:32px"><div class="plate-inner"><span class="rivet" style="left:6px"></span><span class="rivet" style="right:6px"></span><div class="plate-num">100,000</div><div class="plate-unit">STUDENTS</div></div></div>
    <div class="plate" style="left:240px"><div class="plate-inner"><span class="rivet" style="left:6px"></span><span class="rivet" style="right:6px"></span><div class="plate-num">700,000</div><div class="plate-unit">STUDENTS</div></div></div>
    <div class="plate" style="left:453px"><div class="plate-inner"><span class="rivet" style="left:6px"></span><span class="rivet" style="right:6px"></span><div class="plate-num">1,800</div><div class="plate-unit">STUDENTS</div></div></div>

    <svg class="plate-arrow" style="left:115px" width="24" height="66" viewBox="0 0 24 66" aria-hidden="true"><path d="M12 0 V48" stroke="#f5e22a" stroke-width="3" stroke-dasharray="3 4"/><path d="M2 50 H22 L12 64 Z" fill="#f5e22a"/></svg>
    <svg class="plate-arrow" style="left:316px" width="24" height="66" viewBox="0 0 24 66" aria-hidden="true"><path d="M12 0 V48" stroke="#f5e22a" stroke-width="3" stroke-dasharray="3 4"/><path d="M2 50 H22 L12 64 Z" fill="#f5e22a"/></svg>
    <svg class="plate-arrow" style="left:536px" width="24" height="66" viewBox="0 0 24 66" aria-hidden="true"><path d="M12 0 V48" stroke="#f5e22a" stroke-width="3" stroke-dasharray="3 4"/><path d="M2 50 H22 L12 64 Z" fill="#f5e22a"/></svg>

    <div class="outcome" style="left:27px">Are victims of alcohol-related sexual assault or date rape</div>
    <div class="outcome" style="left:230px">Have been assaulted by another student who was under the influence of alcohol</div>
    <div class="outcome" style="left:448px;top:325px">Die each year from alcohol-related unintentional injuries</div>
  </section>

  <section class="footer">
    <div class="abs brand">
      <span class="brand-dot"></span>
      <span class="brand-name">CORAL DUNE RECOVERY</span>
    </div>
  </section>

  <section class="bottom-strip"></section>

</div>
</body>
</html>
```